Dubai, Oman, Saudi, Qatar, Kuwait, Bahrain
OVUX.CA a popular Canadian non profit is opening in the middle east and will require a website that appeals to the Arab world
Industry
Technology
Color Preferences
green and blue and similar to ovux.ca
Our Ideas & Additional Information
use these websites as examples to copy and make similar websites
www.pqz.mg
www.ovux.ca
www.lirovastemo.ba
OVUX Arabic - Zafir Tech (Technology) non profit , foundation , association
Please try to use some arabic writing as well as latin alphabet for the name of the company
Zafir Tech (Technology)
Please see sample logos attached, dont worry about logo design we will add later
Target Market(s)
gcc
Number of Pages Required
1 page
Look and feel

```html
<!DOCTYPE html>
<html lang="en">
<head>
<meta charset="utf-8">
<title>Zafir Tech — Empowering Communities Through Technology</title>
<link href="https://fonts.googleapis.com/css2?family=Audiowide&family=Poppins:ital,wght@0,400;0,500;0,600;0,700;1,400&display=swap" rel="stylesheet">
<style>
:root{
  --navy:#161c5e;
  --navy-deep:#0f1448;
  --green:#0cbf2f;
  --green-dark:#08a526;
  --mint:#e8f7ee;
  --mint-soft:#f1fbf5;
  --ink:#1b1f4a;
  --body:#4a4f6a;
  --white:#ffffff;
}
*{margin:0;padding:0;box-sizing:border-box}
html,body{width:1200px;height:4208px;overflow:hidden}
body{position:relative;font-family:"Poppins",sans-serif;color:var(--body);
  background:linear-gradient(180deg,var(--mint) 0%,var(--mint-soft) 60%,#eef0f6 100%)}
.abs{position:absolute}
.display{font-family:"Audiowide",sans-serif;color:var(--ink);font-weight:400}
.hl{background:var(--green);color:var(--white);padding:0 8px;border-radius:3px}
.btn{position:absolute;display:flex;align-items:center;justify-content:center;font-weight:600;font-size:12px;text-transform:uppercase;letter-spacing:.3px;border-radius:3px}
.btn-green{background:var(--green);color:var(--white)}
.btn-outline{border:2px solid var(--white);color:var(--white)}
.shapes{position:absolute;left:0;top:0}

/* nav */
.brand{left:90px;top:70px;font-family:"Audiowide",sans-serif;color:var(--white);font-size:19px}
.brand-dot{display:inline-block;width:12px;height:12px;border-radius:50%;background:var(--green);margin-right:8px}
.nav{left:390px;top:50px;display:flex;gap:25px;font-size:13.5px;color:var(--white)}
.nav .active{font-weight:600;border-bottom:2px solid var(--white);padding-bottom:2px}
.nav-cta{left:986px;top:42px;width:126px;height:36px;text-transform:none;font-size:13px}

/* hero */
.hero-kicker{left:88px;top:251px;font-family:"Audiowide",sans-serif;color:var(--white);font-size:20px}
.hero-title{left:73px;top:291px;width:528px;height:81px;background:var(--green);border-radius:3px;color:var(--white);font-family:"Audiowide",sans-serif;font-size:66px;line-height:81px;text-align:center}
.hero-text{left:90px;top:392px;width:480px;color:var(--white);font-size:16px;line-height:24px}

/* about */
.kicker{font-size:16px;font-weight:600;color:var(--green-dark)}
.about-title{left:142px;top:818px;font-size:40px;line-height:50px}
.about-text{left:544px;top:772px;width:520px;font-size:13.8px;line-height:23px}
.team-photo{left:124px;top:1004px;width:386px;height:386px;border-radius:50%;background:radial-gradient(circle at 45% 40%,#c9a88b,#7a5a4a 55%,#4b3a45);box-shadow:0 20px 40px rgba(20,30,80,.25)}
.sub-title{font-family:"Audiowide",sans-serif;color:var(--ink);font-size:24px}
.sub-text{font-size:14px;line-height:23px;width:460px}

/* services */
.section-title{left:0;width:1200px;text-align:center;font-size:38px}
.card{position:absolute;top:1574px;width:237px;height:248px;background:var(--white);border-radius:10px;box-shadow:0 8px 30px rgba(20,40,80,.08);text-align:center;padding:24px 18px}
.card .ico{width:64px;height:64px;margin:0 auto 14px;border-radius:12px;background:#e3f6e8;display:flex;align-items:center;justify-content:center}
.card h3{font-family:"Audiowide",sans-serif;font-weight:400;font-size:14px;line-height:17px;color:var(--ink);margin-bottom:8px}
.card p{font-size:12px;line-height:18px}
.round{position:absolute;border-radius:50%;display:flex;align-items:center;justify-content:center;color:var(--white)}

/* why */
.why-item{position:absolute;font-family:"Audiowide",sans-serif;font-size:15px;line-height:18px;color:var(--ink)}
.why-ico{position:absolute;width:66px;height:66px;border-radius:50%;background:var(--white);box-shadow:0 6px 20px rgba(20,40,80,.12);display:flex;align-items:center;justify-content:center}
.emblem{left:443px;top:2110px;width:300px;height:300px;border-radius:50%;background:var(--navy);display:flex;align-items:center;justify-content:center;font-family:"Audiowide",sans-serif;color:var(--white);font-size:34px}

/* partners */
.partner-title{left:118px;top:2543px;font-size:38px;color:var(--white)}
.view-all{left:885px;top:2541px;width:196px;height:57px;font-size:13px}
.pcard{position:absolute;background:var(--white);border-radius:12px;box-shadow:0 12px 30px rgba(0,0,0,.15);padding:30px 22px}
.pcard h3{font-family:"Audiowide",sans-serif;font-weight:400;font-size:19px;color:var(--ink);margin-bottom:10px}
.pcard p{font-size:12px;line-height:19px;width:400px}
.pcard .photo{margin-top:20px;width:412px;height:227px;border-radius:10px}

/* testimonial */
.quote{left:129px;top:3310px;width:490px;font-style:italic;font-size:22px;line-height:36px;color:#3a3f5f}
.qmark{font-family:"Audiowide",sans-serif;color:var(--green);font-size:52px;line-height:1}
.author{left:798px;top:3352px;font-family:"Audiowide",sans-serif;font-size:19px;line-height:22px;color:var(--ink)}

/* cta */
.cta{left:134px;top:3534px;width:932px;height:168px;background:var(--green);border-radius:8px}
.cta h2{position:absolute;left:59px;top:50px;font-family:"Audiowide",sans-serif;font-weight:400;color:var(--white);font-size:42px}
.cta p{position:absolute;left:59px;top:102px;font-family:"Audiowide",sans-serif;color:var(--white);font-size:22px}

/* footer */
.foot-brand{left:138px;top:3955px;font-family:"Audiowide",sans-serif;color:var(--navy);font-size:30px}
.foot-mark{left:210px;top:3870px;width:56px;height:56px;border-radius:50%;background:var(--navy)}
.foot-col h4{font-family:"Audiowide",sans-serif;font-weight:400;color:var(--ink);font-size:18px;margin-bottom:18px}
.foot-col li{list-style:none;font-size:17px;line-height:36px;color:#2a2e52}
.contact-label{font-size:13px;font-weight:600;color:var(--green-dark)}
.contact-value{font-size:13px;color:#2a2e52}
.rule{left:90px;top:4153px;width:1020px;height:1px;background:#c9ccd8}
.copyright{left:0;top:4170px;width:1200px;text-align:center;font-size:15px;color:#2a2e52}
</style>
</head>
<body>

<!-- background bands -->
<svg class="shapes" width="1200" height="4208" viewBox="0 0 1200 4208" aria-hidden="true">
  <defs>
    <linearGradient id="heroGrad" x1="0" y1="0" x2="0" y2="1">
      <stop offset="0" stop-color="#242d7e"/><stop offset="1" stop-color="#161c5e"/>
    </linearGradient>
  </defs>
  <polygon points="0,0 1200,0 1200,505 0,675" fill="url(#heroGrad)"/>
  <polygon points="0,675 1200,505 1200,528 0,718" fill="var(--green)"/>
  <polygon points="0,1305 1200,1455 1200,2300 0,2430" fill="#ffffff"/>
  <polygon points="380,1360 1200,1430 1200,1462" fill="var(--navy)"/>
  <polygon points="0,2425 1200,2288 1200,2318 0,2475" fill="var(--green)"/>
  <polygon points="0,2475 1200,2318 1200,3035 0,2990" fill="var(--navy)"/>
  <polygon points="980,3040 1200,3030 1200,3064" fill="var(--green)"/>
  <polygon points="0,3740 212,3703 0,3776" fill="var(--navy)"/>
</svg>

<!-- header -->
<div class="abs brand"><span class="brand-dot"></span>Zafir Tech</div>
<nav class="abs nav">
  <span class="active">HOME</span><span>About Us</span><span>Services</span><span>Donate Devices</span><span>Impact</span><span>Partners</span><span>Contact</span>
</nav>
<div class="btn btn-green nav-cta">Donate Now</div>

<!-- hero -->
<svg class="abs" style="left:510px;top:100px" width="690" height="600" viewBox="0 0 690 600" role="img" aria-label="Photo of a modern skyscraper above a city skyline, framed in a large triangle">
  <defs>
    <linearGradient id="tower" x1="0" y1="0" x2="0" y2="1">
      <stop offset="0" stop-color="#8f98b0"/><stop offset=".55" stop-color="#5d6a80"/><stop offset="1" stop-color="#a79f91"/>
    </linearGradient>
  </defs>
  <polygon points="10,590 326,14 670,590" fill="url(#tower)"/>
  <polygon points="560,410 690,420 690,590 640,590" fill="#e8f7ee"/>
</svg>
<div class="abs hero-kicker">Empowering Communities Through</div>
<div class="abs hero-title">Technology</div>
<p class="abs hero-text">Sustainable IT solutions that bridge the digital divide and reduce e-waste across the Middle East.</p>
<div class="btn btn-green" style="left:90px;top:460px;width:160px;height:38px">Donate Devices</div>
<div class="btn btn-outline" style="left:258px;top:460px;width:155px;height:38px">Partner With Us</div>

<!-- about -->
<div class="abs kicker" style="left:142px;top:786px">About Us</div>
<h2 class="abs display about-title">Technology<br>with <span class="hl">Purpose</span></h2>
<p class="abs about-text">Zafir Tech is a nonprofit organization committed to refurbishing and redistributing used electronics to underserved communities across the Gulf region. By diverting electronic waste from landfills, we create meaningful digital access opportunities while promoting environmental sustainability. We believe access to technology is a human right — not a privilege. That's why we work with individuals, schools, nonprofits, and businesses to make digital inclusion a reality for all.</p>

<div class="abs team-photo" role="img" aria-label="Photo of smiling volunteers holding a donation box of devices"></div>
<h3 class="abs sub-title" style="left:583px;top:1052px">Our Vision</h3>
<p class="abs sub-text" style="left:583px;top:1096px">A digitally connected and environmentally responsible Middle East.</p>
<h3 class="abs sub-title" style="left:583px;top:1164px">Our Mission</h3>
<p class="abs sub-text" style="left:583px;top:1208px">To reduce e-waste and promote digital equity through secure electronics recycling, refurbishing, and redistribution.</p>
<div class="btn btn-green" style="left:583px;top:1280px;width:126px;height:36px">Learn More</div>

<!-- services -->
<h2 class="abs display section-title" style="top:1488px">What We <span class="hl">Do</span></h2>
<div class="card" style="left:105px">
  <div class="ico"><svg width="36" height="36" viewBox="0 0 36 36" fill="none" stroke="#0cbf2f" stroke-width="2"><rect x="8" y="5" width="20" height="26" rx="2"/><path d="M12 12h12M12 17h12M12 22h7"/></svg></div>
  <h3>Secure IT Asset<br>Disposition (ITAD)</h3>
  <p>We safely collect, track, and process your retired IT equipment. Your data is securely destroyed.</p>
</div>
<div class="card" style="left:356px">
  <div class="ico"><svg width="36" height="36" viewBox="0 0 36 36" fill="none" stroke="#0cbf2f" stroke-width="2"><circle cx="18" cy="18" r="12"/><path d="M12 18l4 4 8-8"/></svg></div>
  <h3>Certified<br>Data Destruction</h3>
  <p>We follow international standards (ISO 27001, ISO 9001) to ensure that all data is wiped or destroyed using</p>
</div>
<div class="card" style="left:607px">
  <div class="ico"><svg width="36" height="36" viewBox="0 0 36 36" fill="none" stroke="#0cbf2f" stroke-width="2"><path d="M18 31s-9-9-9-16a9 9 0 0118 0c0 7-9 16-9 16z"/><circle cx="18" cy="15" r="3"/></svg></div>
  <h3>Refurbishment<br>&amp; Redistribution</h3>
  <p>We restore donated devices and give them new life by distributing them to students, nonprofits, and low</p>
</div>
<div class="card" style="left:859px">
  <div class="ico"><svg width="36" height="36" viewBox="0 0 36 36" fill="none" stroke="#0cbf2f" stroke-width="2"><circle cx="18" cy="12" r="4"/><circle cx="9" cy="16" r="3"/><circle cx="27" cy="16" r="3"/><path d="M10 30c0-5 3.5-8 8-8s8 3 8 8M3 28c0-3 2.5-5 6-5M33 28c0-3-2.5-5-6-5"/></svg></div>
  <h3>Community<br>Impact Programs</h3>
  <p>We host free digital literacy workshops, tech skills training, &amp; device donation programs across the region</p>
</div>
<div class="round" style="left:556px;top:1847px;width:40px;height:40px;background:var(--navy);font-size:14px">&#8249;</div>
<div class="round" style="left:604px;top:1847px;width:40px;height:40px;background:var(--green);font-size:14px">&#8250;</div>

<!-- why choose -->
<h2 class="abs display section-title" style="top:1947px">Why <span class="hl">Choose</span> Zafir Tech</h2>
<div class="abs emblem">Zafir Tech</div>

<div class="why-item" style="right:785px;top:2079px;text-align:right">Certified Secure<br>Processing</div>
<div class="why-ico" style="left:437px;top:2064px"><svg width="30" height="30" viewBox="0 0 30 30" fill="none" stroke="#0cbf2f" stroke-width="2"><circle cx="15" cy="15" r="11"/><path d="M10 15l3.5 3.5L20 12"/></svg></div>
<div class="why-item" style="right:843px;top:2186px;text-align:right">Transparent<br>Chain of Custody</div>
<div class="why-ico" style="left:387px;top:2171px"><svg width="30" height="30" viewBox="0 0 30 30" fill="none" stroke="#0cbf2f" stroke-width="2"><rect x="5" y="11" width="11" height="8" rx="4"/><rect x="14" y="11" width="11" height="8" rx="4"/></svg></div>
<div class="why-item" style="right:880px;top:2293px;text-align:right">Environmental<br>Compliance</div>
<div class="why-ico" style="left:343px;top:2278px"><svg width="30" height="30" viewBox="0 0 30 30" fill="none" stroke="#0cbf2f" stroke-width="2"><path d="M15 4l9 4v7c0 6-4 10-9 12-5-2-9-6-9-12V8z"/><path d="M11 15l3 3 5-6"/></svg></div>

<div class="why-ico" style="left:684px;top:2064px"><svg width="30" height="30" viewBox="0 0 30 30" fill="none" stroke="#0cbf2f" stroke-width="2"><circle cx="15" cy="15" r="11"/><path d="M4 15h22M15 4c4 4 4 18 0 22M15 4c-4 4-4 18 0 22"/></svg></div>
<div class="why-item" style="left:771px;top:2079px">Local &amp; Regional<br>Impact</div>
<div class="why-ico" style="left:734px;top:2164px"><svg width="30" height="30" viewBox="0 0 30 30" fill="none" stroke="#0cbf2f" stroke-width="2"><path d="M4 16l6-6 5 3 5-3 6 6-8 7-4-3-4 3z"/></svg></div>
<div class="why-item" style="left:820px;top:2177px">Customized<br>Corporate Reporting</div>
<div class="why-ico" style="left:778px;top:2260px"><svg width="30" height="30" viewBox="0 0 30 30" fill="none" stroke="#0cbf2f" stroke-width="2"><circle cx="15" cy="15" r="11"/><path d="M9 18c3-1 4-5 8-6M18 22c0-3 2-5 5-5"/></svg></div>
<div class="why-item" style="left:862px;top:2273px">ESG Alignment &amp;<br>CSR Support</div>

<!-- partners -->
<h2 class="abs display partner-title">Who We <span class="hl">Work With</span></h2>
<div class="btn btn-outline view-all">View All Project</div>

<div class="pcard" style="left:118px;top:2662px;width:454px;height:372px">
  <h3>Corporate Partners</h3>
  <p>We work with responsible businesses seeking to dispose of IT assets securely while supporting local communities.</p>
  <div class="photo" role="img" aria-label="Photo of business people shaking hands outside a modern office" style="background:linear-gradient(135deg,#b9a58e,#5e6b7c 60%,#2f3646)"></div>
</div>
<div class="round" style="left:526px;top:2633px;width:78px;height:78px;background:var(--green)"><svg width="28" height="28" viewBox="0 0 28 28" fill="none" stroke="#fff" stroke-width="2.2"><path d="M7 21L21 7M10 7h11v11"/></svg></div>

<div class="pcard" style="left:596px;top:2722px;width:452px;height:373px">
  <h3>Educational Institutions</h3>
  <p>Schools and universities benefit from our refurbished computers, laptops, and classroom-ready technology bundles.</p>
  <div class="photo" role="img" aria-label="Photo of students walking down campus steps with notebooks" style="background:linear-gradient(135deg,#9aa5b4,#5a6478 55%,#a0967f)"></div>
</div>
<div class="round" style="left:1003px;top:2695px;width:78px;height:78px;background:var(--green)"><svg width="28" height="28" viewBox="0 0 28 28" fill="none" stroke="#fff" stroke-width="2.2"><path d="M7 21L21 7M10 7h11v11"/></svg></div>

<!-- testimonial -->
<h2 class="abs display section-title" style="top:3182px">What Our <span class="hl">Clients Say</span></h2>
<div class="abs qmark" style="left:90px;top:3290px">&ldquo;</div>
<p class="abs quote">Thanks to Zafir Tech, our school received refurbished laptops that have transformed our classrooms. The students are now more engaged and digitally empowered</p>
<div class="abs qmark" style="left:583px;top:3412px">&rdquo;</div>
<div class="abs" style="left:686px;top:3328px;width:88px;height:88px;border-radius:50%;background:linear-gradient(135deg,#6b6f7a,#2c2f38)" role="img" aria-label="Portrait photo of the school principal"></div>
<div class="abs author">Principal, Gulf<br>Regional School</div>
<div class="round" style="left:1042px;top:3320px;width:48px;height:48px;background:var(--navy);font-size:18px">&#8250;</div>
<div class="round" style="left:1042px;top:3376px;width:48px;height:48px;background:var(--green);font-size:18px">&#8249;</div>

<!-- call to action -->
<div class="abs cta">
  <h2>Have Unused Tech?</h2>
  <p>Let's Turn It Into Opportunity</p>
  <div class="btn btn-outline" style="left:694px;top:59px;width:176px;height:52px">Request Pickup</div>
</div>

<!-- footer -->
<div class="abs foot-mark"></div>
<div class="abs foot-brand">Zafir Tech</div>

<div class="abs foot-col" style="left:413px;top:3802px">
  <h4>Quick Links</h4>
  <ul><li>Home</li><li>About Us</li><li>Services</li><li>Donate Devices</li><li>Impact</li><li>Partners</li><li>Contact</li></ul>
</div>
<div class="abs foot-col" style="left:640px;top:3802px">
  <h4>Donation</h4>
  <ul><li>E-waste drive events</li><li>Shipping labels</li><li>Same Day Pick Up</li><li>Request</li><li>Collect for us</li><li>Recycling Depots</li><li>Book a pick up</li></ul>
</div>
<div class="abs foot-col" style="left:903px;top:3802px">
  <h4>Contact Us</h4>
  <div style="display:flex;gap:10px">
    <svg width="16" height="14" viewBox="0 0 16 14" fill="none" stroke="#0cbf2f" stroke-width="1.8"><rect x="1" y="1" width="14" height="12" rx="1"/><path d="M1 2l7 6 7-6"/></svg>
    <div><div class="contact-label">Email:</div><div class="contact-value">info@example.com</div></div>
  </div>
  <div style="display:flex;gap:10px;margin-top:18px">
    <svg width="16" height="16" viewBox="0 0 16 16" fill="none" stroke="#0cbf2f" stroke-width="1.8"><path d="M3 1l3 3-2 2c1 2 3 4 5 5l2-2 3 3-2 3C7 15 1 9 1 3z"/></svg>
    <div><div class="contact-label">Phone:</div><div class="contact-value">(012) 555 - 0147</div></div>
  </div>
  <h4 style="margin-top:20px;margin-bottom:10px">Follow Us</h4>
  <div style="display:flex;gap:8px;align-items:center"><span style="width:10px;height:10px;background:var(--green)"></span><span class="contact-value" style="text-decoration:underline">Social Profile</span></div>
</div>

<div class="abs rule"></div>
<div class="abs copyright">&copy;Copyright 2025 Zafir Tech | All Rights Reserved</div>
<div class="round" style="left:1132px;top:4125px;width:48px;height:48px;background:var(--green);font-size:18px">&#8963;</div>

</body>
</html>
```